Fun and Splashy Flyer Design

We need a flyer designed for our new car cleaning brand! We have looked around, and the stock options either look way too dark/serious/exclusive, or they look too shiny/stock image.

We need something that can be more subtle, that works with our work van.

For this project we would like a photoshop file with individual layers, and you can just put placeholder text for the main slogan, a header 1, header 2, bullet point and body text.

What we're really looking for are the transitions between images and elements, font colours and pairings and design accents.

We want the brand to be fun, clean, happy and straightforward (slightly minimalist). Please message if you have any questions!

```html
<!DOCTYPE html>
<html lang="en">
<head>
<meta charset="utf-8">
<title>Brightside Wash – Mobile Car Cleaning Flyer</title>
<link href="https://fonts.googleapis.com/css2?family=Fredoka:wght@600;700&family=Open+Sans:wght@700&display=swap" rel="stylesheet">
<style>
  :root {
    --royal: #2459a8;
    --navy: #1f3f78;
    --sun: #f9c31f;
    --sun-deep: #d69a14;
    --orange: #f28a22;
    --white: #ffffff;
  }
  * { box-sizing: border-box; margin: 0; padding: 0; }
  html, body { width: 848px; height: 1200px; overflow: hidden; background: var(--white); }
  .flyer { position: relative; width: 848px; height: 1200px; overflow: hidden; background: var(--royal); font-family: "Open Sans", Arial, sans-serif; }

  .top-band { position: absolute; left: 0; top: 0; width: 848px; height: 137px; background: var(--royal); }
  .brand { position: absolute; left: 22px; top: 32px; width: 130px; display: flex; align-items: center; gap: 8px; }
  .brand-dot { width: 22px; height: 22px; border-radius: 50%; background: var(--sun); flex: none; }
  .brand-name { font-family: "Fredoka", Arial, sans-serif; font-weight: 700; font-size: 19px; line-height: 1.1; color: var(--white); }
  .service-title { position: absolute; left: 168px; top: 30px; font-family: "Fredoka", Arial, sans-serif; font-weight: 700; font-size: 50px; letter-spacing: 1px; color: var(--white); white-space: nowrap; }
  .service-title .accent { color: var(--sun); }

  .side-texture { position: absolute; top: 137px; height: 945px; }
  .side-texture.left { left: 0; width: 70px; background: linear-gradient(180deg, var(--sun) 0%, var(--orange) 18%, var(--royal) 30%, var(--sun) 48%, var(--orange) 60%, var(--royal) 74%, var(--sun) 88%, var(--royal) 100%); }
  .side-texture.right { left: 761px; width: 87px; background: linear-gradient(180deg, var(--royal) 0%, var(--sun) 14%, var(--orange) 30%, var(--royal) 44%, var(--sun) 60%, var(--orange) 76%, var(--sun) 88%, var(--royal) 100%); }

  .panel { position: absolute; left: 70px; top: 137px; width: 691px; height: 945px; background: var(--white); }
  .slogan { position: absolute; left: 0; width: 100%; text-align: center; font-family: "Fredoka", Arial, sans-serif; font-weight: 700; }
  .slogan.main { top: 42px; font-size: 58px; color: var(--navy); }
  .slogan.sub { top: 108px; font-size: 50px; color: var(--sun); }

  .hero-art { position: absolute; left: 165px; top: 211px; width: 375px; height: 240px; border-radius: 40% 45% 30% 35%; background: radial-gradient(ellipse at 50% 55%, #2f5fb0 0%, #4f78c0 40%, #dfe6f0 75%, var(--white) 100%); }

  .header-one { position: absolute; left: 0; top: 488px; width: 100%; text-align: center; font-family: "Fredoka", Arial, sans-serif; font-weight: 700; font-size: 46px; color: var(--navy); }
  .header-two { position: absolute; left: 0; top: 556px; width: 100%; text-align: center; font-family: "Fredoka", Arial, sans-serif; font-weight: 700; font-size: 37px; color: var(--sun); }

  .points { position: absolute; left: 46px; top: 637px; list-style: none; }
  .points li { position: relative; padding-left: 45px; font-size: 20px; line-height: 31.1px; color: var(--navy); }
  .points li::before { content: ""; position: absolute; left: 2px; top: 12px; width: 7px; height: 7px; border-radius: 50%; background: var(--navy); }

  .sponge { position: absolute; left: 213px; top: 617px; width: 466px; height: 286px; }
  .sponge svg { position: absolute; inset: 0; }
  .sponge-text { position: absolute; left: 29px; top: 50px; width: 415px; font-size: 13.4px; line-height: 21.8px; color: var(--white); }

  .bottom-band { position: absolute; left: 0; top: 1082px; width: 848px; height: 118px; background: var(--royal); }
  .call { position: absolute; left: 0; top: 26px; width: 100%; text-align: center; font-family: "Fredoka", Arial, sans-serif; font-weight: 700; font-size: 54px; letter-spacing: 2px; color: var(--white); }
</style>
</head>
<body>
<div class="flyer">
  <header class="top-band">
    <div class="brand"><span class="brand-dot"></span><span class="brand-name">Brightside Wash</span></div>
    <h1 class="service-title">MOBILE CAR <span class="accent">CLEANING</span></h1>
  </header>

  <div class="side-texture left" role="img" aria-label="Swirling blue, yellow and orange paint texture"></div>
  <div class="side-texture right" role="img" aria-label="Swirling blue, yellow and orange paint texture"></div>

  <main class="panel">
    <h2 class="slogan main">Main Slogan</h2>
    <p class="slogan sub">Text</p>

    <div class="hero-art" role="img" aria-label="Illustration of a blue car being washed by a mobile cleaning crew"></div>

    <h3 class="header-one">Header one</h3>
    <h4 class="header-two">Header two</h4>

    <ul class="points">
      <li>Point 1</li><li>Point 2</li><li>Point 3</li><li>Point 4</li>
      <li>Point 5</li><li>Point 6</li><li>Point 7</li><li>Point 8</li>
    </ul>

    <div class="sponge">
      <svg viewBox="0 0 466 286" width="466" height="286" aria-hidden="true">
        <path d="M40 22 C120 4 170 30 240 24 C320 16 380 -4 430 30 C470 58 440 110 452 160 C466 220 440 270 380 274 C310 280 260 250 190 264 C120 278 50 286 24 240 C2 200 30 160 14 110 C0 66 6 30 40 22 Z" fill="var(--sun-deep)"/>
        <path d="M46 34 C124 18 172 42 240 36 C318 28 376 10 420 40 C454 64 428 112 440 160 C452 214 430 256 378 260 C310 266 260 236 190 250 C122 264 60 272 38 234 C18 198 44 160 28 112 C16 72 18 42 46 34 Z" fill="var(--sun)"/>
      </svg>
      <p class="sponge-text">Lorem ipsum dolor sit amet, consectetur adipiscing elit, sed do eiusmod tempor incididunt ut labore et dolore magna aliqua. Ut enim ad minim veniam, quis nostrud exercitation ullamco laboris nisi ut aliquip ex ea commodo consequat. Duis aute irure dolor in reprehenderit in voluptate velit esse cillum dolore eu fugiat nulla pariatur. Excepteur sint occaecat cupidatat non proident, sunt in culpa qui officia deserunt mollit anim id est laborum.</p>
    </div>
  </main>

  <footer class="bottom-band">
    <p class="call">CALL 0400-555-210</p>
  </footer>
</div>
</body>
</html>
```